Bakersfield's Grand Dash 2015 POSTER

Looking for a hip design to attract young 20-30 somethings to a downtown scavenger hunt as a benefit for a local non-profit. Please see our website at www.granddashfun.org. Race Date is March 14, 2015, in Downtown Bakersfield.

```html
<!DOCTYPE html>
<html lang="en">
<head>
<meta charset="utf-8">
<title>Grand Dash 2015 – Scavenger Hunt Poster</title>
<link rel="stylesheet" href="https://fonts.googleapis.com/css2?family=Orbitron:wght@700;900&display=swap">
<style>
  :root {
    --paper-light: #f1e6c6;
    --paper-mid: #e6d29f;
    --paper-edge: #a8743a;
    --paper-burn: #6e4419;
    --ink-light: #37b4e6;
    --ink-mid: #1f7cc9;
    --ink-deep: #0d3c96;
    --halo: #ffffff;
    --lens: #e9e9e9;
    --lens-shade: #c9c9c9;
  }
  html, body {
    margin: 0;
    padding: 0;
    width: 848px;
    height: 1200px;
    overflow: hidden;
  }
  .poster {
    position: relative;
    width: 848px;
    height: 1200px;
    overflow: hidden;
    font-family: "Orbitron", sans-serif;
    background:
      radial-gradient(ellipse at 50% 50%, var(--paper-light) 0%, var(--paper-mid) 62%, var(--paper-edge) 90%, var(--paper-burn) 100%);
  }
  .ink {
    position: absolute;
    margin: 0;
    white-space: nowrap;
    text-transform: uppercase;
    color: var(--ink-mid);
    background: linear-gradient(180deg, var(--ink-light) 0%, var(--ink-mid) 50%, var(--ink-deep) 100%);
    -webkit-background-clip: text;
    background-clip: text;
    -webkit-text-fill-color: transparent;
    filter:
      drop-shadow(2px 0 0 var(--halo)) drop-shadow(-2px 0 0 var(--halo))
      drop-shadow(0 2px 0 var(--halo)) drop-shadow(0 -2px 0 var(--halo));
  }
  .title {
    left: 0;
    width: 848px;
    text-align: center;
    font-weight: 900;
    font-size: 112px;
    line-height: 1;
    letter-spacing: 2px;
  }
  .title--first { top: 50px; }
  .title--second { top: 216px; }

  .details {
    left: 43px;
    font-weight: 900;
    font-size: 46px;
    line-height: 1;
    letter-spacing: 1px;
  }
  .details--hunt { top: 398px; }
  .details--in { top: 478px; }
  .details--downtown { top: 552px; }
  .details--city { top: 628px; }
  .details--date { top: 782px; }

  .tagline {
    left: 0;
    width: 848px;
    text-align: center;
    font-weight: 900;
    font-size: 76px;
    line-height: 1;
    letter-spacing: -1px;
  }
  .tagline--one { top: 920px; }
  .tagline--two { top: 1004px; }
  .tagline--three { top: 1082px; }

  .magnifier {
    position: absolute;
    left: 540px;
    top: 462px;
    width: 290px;
    height: 380px;
  }
</style>
</head>
<body>
  <main class="poster">
    <h1 class="ink title title--first">Grand</h1>
    <h1 class="ink title title--second">Dash</h1>

    <p class="ink details details--hunt">A scavenger hunt</p>
    <p class="ink details details--in">in</p>
    <p class="ink details details--downtown">Downtown</p>
    <p class="ink details details--city">Bakersfield</p>
    <p class="ink details details--date">14th March 2015</p>

    <svg class="magnifier" viewBox="0 0 290 380" aria-hidden="true">
      <defs>
        <linearGradient id="lens-fill" x1="0" y1="0" x2="0" y2="1">
          <stop offset="0" stop-color="var(--lens-shade)"/>
          <stop offset="1" stop-color="#fafafa"/>
        </linearGradient>
        <linearGradient id="handle-fill" x1="0" y1="0" x2="1" y2="1">
          <stop offset="0" stop-color="var(--ink-mid)"/>
          <stop offset="1" stop-color="var(--ink-deep)"/>
        </linearGradient>
      </defs>
      <line x1="152" y1="185" x2="262" y2="358" stroke="url(#handle-fill)" stroke-width="18" stroke-linecap="round"/>
      <circle cx="101" cy="102" r="86" fill="url(#lens-fill)" stroke="var(--ink-light)" stroke-width="14"/>
    </svg>

    <p class="ink tagline tagline--one">Be a winner.</p>
    <p class="ink tagline tagline--two">The hunt</p>
    <p class="ink tagline tagline--three">is on.</p>
  </main>
</body>
</html>
```